Management Company Needs Web Banners

We need a new set of pixtrel banners developed. Here is what we would like to have:

1. Connect the branding with tangram images from www.VelmarShifts.com
2. Have a "Call to Action" like a "LET'S TALK" Button

1. 728x90 Investments Need Expert Management.
2. 300x250 Senior Living Turnaround Experts
3. 728x90 KIRV Finds Lost Revenue in Senior Living Investments
4. 600x315 Senior Living Turnaround Experts

Target Market(s)

Private Equity, Health Care REITs, physicians, pharmacist, etc.

Industry/Entity Type

Management Consulting

Requirements
Must have
• A branding connection to https://www.VelmarShifts.com/

```html
<!DOCTYPE html>
<html lang="en">
<head>
<meta charset="utf-8">
<title>KIRV Web Banner Set</title>
<link href="https://fonts.googleapis.com/css2?family=Questrial&display=swap" rel="stylesheet">
<style>
  :root {
    --board: #ebebeb;
    --navy: #0b0620;
    --black: #000000;
    --mint: #d5eee9;
    --logo-bg: #f6f6f8;
    --brand: #4a1a5c;
    --white: #ffffff;
    --sky: #7fa6d0;
    --facade: #a08a6e;
    --lawn: #5d8a3a;
  }
  * { margin: 0; padding: 0; box-sizing: border-box; }
  html, body { width: 1087px; height: 1200px; overflow: hidden; background: var(--board); }
  body { position: relative; font-family: "Questrial", sans-serif; color: var(--white); }

  .banner { position: absolute; overflow: hidden; box-shadow: 3px 5px 6px rgba(0,0,0,.35); }
  .banner svg.backdrop { position: absolute; inset: 0; width: 100%; height: 100%; }
  .banner > div, .banner > a { position: absolute; }

  .logo { display: flex; align-items: center; gap: 4px; color: var(--brand); }
  .logo-dot { border-radius: 50%; background: var(--brand); }
  .cta {
    border: 1.5px solid var(--white); color: var(--white); text-align: center;
    text-transform: uppercase; white-space: nowrap; text-decoration: none; display: flex;
    align-items: center; justify-content: center; letter-spacing: -.02em;
  }
  .cta.on-mint { border-color: var(--navy); color: var(--navy); }
  .url { white-space: nowrap; }

  /* Skyscraper */
  .skyscraper { left: 167px; top: 257px; width: 96px; height: 438px; background: var(--mint); }
  .skyscraper .logo { left: 36px; top: 15px; font-size: 11px; }
  .skyscraper .logo-dot { width: 12px; height: 12px; }
  .skyscraper .headline { left: 0; width: 96px; top: 194px; font-size: 14.5px; line-height: 25px; text-align: center; }
  .skyscraper .cta { left: 19px; top: 381px; width: 56px; height: 13px; font-size: 7px; }
  .skyscraper .cta.on-mint { border-width: 1px; }
  .skyscraper .url { left: 0; width: 96px; top: 405px; font-size: 7px; text-align: center; color: var(--navy); letter-spacing: -.03em; }

  /* Leaderboard */
  .leaderboard { left: 296px; top: 257px; width: 714px; height: 89px; background: var(--mint); }
  .leaderboard .logo { left: 13px; top: 16px; font-size: 18px; }
  .leaderboard .logo-dot { width: 20px; height: 20px; }
  .leaderboard .headline { left: 270px; width: 340px; top: 9px; font-size: 26px; line-height: 22px; text-align: center; }
  .leaderboard .url { left: 270px; width: 340px; top: 66px; font-size: 13.5px; text-align: center; }
  .leaderboard .cta { left: 634px; top: 38px; width: 68px; height: 15px; font-size: 9px; }

  /* Medium rectangle */
  .rectangle { left: 309px; top: 406px; width: 252px; height: 200px; background: var(--mint); }
  .rectangle .logo { left: 13px; top: 13px; font-size: 15px; }
  .rectangle .logo-dot { width: 16px; height: 16px; }
  .rectangle .headline { left: 11px; top: 84px; font-size: 21px; line-height: 25px; }
  .rectangle .cta { left: 166px; top: 141px; width: 63px; height: 13px; font-size: 7.5px; border-width: 1px; }
  .rectangle .url { left: 10px; top: 178px; font-size: 10px; color: var(--navy); }

  /* Social card */
  .social { left: 302px; top: 627px; width: 551px; height: 288px; background: var(--mint); }
  .social .logo { left: 16px; top: 17px; font-size: 20px; }
  .social .logo-dot { width: 22px; height: 22px; }
  .social .headline { left: 246px; width: 280px; top: 40px; font-size: 37px; line-height: 44px; text-align: center; }
  .social .cta { left: 356px; top: 198px; width: 105px; height: 24px; font-size: 15px; text-transform: none; }
  .social .url { left: 314px; width: 200px; top: 244px; font-size: 16px; text-align: center; }
</style>
</head>
<body>

<!-- Skyscraper -->
<section class="banner skyscraper">
  <svg class="backdrop" viewBox="0 0 96 438" preserveAspectRatio="none">
    <defs>
      <linearGradient id="sky-photo" x1="0" y1="0" x2="0" y2="1">
        <stop offset="0" stop-color="#9cb7d4"/><stop offset=".45" stop-color="#9a7a62"/><stop offset="1" stop-color="#5d8a3a"/>
      </linearGradient>
    </defs>
    <rect class="photo" role="img" aria-label="Photo of a brick suburban house with lawn" x="0" y="40" width="96" height="135" fill="url(#sky-photo)"/>
    <polygon points="0,0 96,0 96,58 0,43" fill="var(--logo-bg)"/>
    <polygon points="0,171 96,149 96,343 0,362" fill="var(--black)"/>
  </svg>
  <div class="logo"><span class="logo-dot"></span>KIRV</div>
  <div class="headline">Finds Lost<br>Revenue<br>in Senior<br>Living<br>Investments</div>
  <a class="cta on-mint" href="#">Let's Talk</a>
  <div class="url">www.VelmarShifts.com</div>
</section>

<!-- Leaderboard -->
<section class="banner leaderboard">
  <svg class="backdrop" viewBox="0 0 714 89" preserveAspectRatio="none">
    <defs>
      <linearGradient id="lead-photo" x1="0" y1="0" x2="0" y2="1">
        <stop offset="0" stop-color="#7fa6d0"/><stop offset=".5" stop-color="#a08a6e"/><stop offset="1" stop-color="#6b5a4a"/>
      </linearGradient>
    </defs>
    <rect role="img" aria-label="Photo of a large two-storey stucco house" x="0" y="0" width="300" height="89" fill="url(#lead-photo)"/>
    <polygon points="0,7 118,7 118,57 0,57" fill="var(--logo-bg)"/>
    <polygon points="242,0 594,0 644,89 292,89" fill="var(--navy)"/>
  </svg>
  <div class="logo"><span class="logo-dot"></span>KIRV</div>
  <div class="headline">Investments Need Expert<br>Management</div>
  <div class="url">www.VelmarShifts.com</div>
  <a class="cta on-mint" href="#">Let's Talk</a>
</section>

<!-- Medium rectangle -->
<section class="banner rectangle">
  <svg class="backdrop" viewBox="0 0 252 200" preserveAspectRatio="none">
    <defs>
      <linearGradient id="rect-photo" x1="0" y1="0" x2="0" y2="1">
        <stop offset="0" stop-color="#7fa6d0"/><stop offset=".55" stop-color="#a08a6e"/><stop offset="1" stop-color="#5d8a3a"/>
      </linearGradient>
    </defs>
    <rect role="img" aria-label="Photo of a large two-storey stucco house" x="0" y="0" width="252" height="120" fill="url(#rect-photo)"/>
    <polygon points="0,0 99,0 99,40 86,54 0,54" fill="var(--logo-bg)"/>
    <polygon points="0,52 252,114 252,169 0,169" fill="var(--navy)"/>
  </svg>
  <div class="logo"><span class="logo-dot"></span>KIRV</div>
  <div class="headline">Senior Living<br>Turnaround<br>Experts</div>
  <a class="cta" href="#">Let's Talk</a>
  <div class="url">www.VelmarShifts.com</div>
</section>

<!-- Social card -->
<section class="banner social">
  <svg class="backdrop" viewBox="0 0 551 288" preserveAspectRatio="none">
    <defs>
      <linearGradient id="social-photo" x1="0" y1="0" x2="0" y2="1">
        <stop offset="0" stop-color="#7fa6d0"/><stop offset=".3" stop-color="#5b6170"/><stop offset=".5" stop-color="#a08a6e"/><stop offset=".9" stop-color="#8a7560"/><stop offset="1" stop-color="#5d8a3a"/>
      </linearGradient>
    </defs>
    <rect role="img" aria-label="Photo of a large two-storey stucco house with arched windows" x="0" y="0" width="320" height="288" fill="url(#social-photo)"/>
    <polygon points="0,0 133,0 101,62 0,62" fill="var(--logo-bg)"/>
    <polygon points="232,0 498,0 551,153 551,288 304,288" fill="var(--black)"/>
  </svg>
  <div class="logo"><span class="logo-dot"></span>KIRV</div>
  <div class="headline">Senior Living<br>Turnaround<br>Experts</div>
  <a class="cta" href="#">LET'S TALK</a>
  <div class="url">www.VelmarShifts.com</div>
</section>

</body>
</html>
```